Harborline Motors LLC

Car Dealer Customer Service
Address: 2741 Linden Avenue, Shelbyville, TN 37162
web: www.harborlinemotorstn.net
email: harborlinemotorstn@mailbox-example.net
Phone: (931) 555-0148
Phone: (629) 555-0173

```html
<!DOCTYPE html>
<html lang="en">
<head>
<meta charset="utf-8">
<title>Harborline Motors – Business Card</title>
<link href="https://fonts.googleapis.com/css2?family=Montserrat:wght@400;500;800&display=swap" rel="stylesheet">
<style>
  :root {
    --stage: #2b2c2e;
    --brand-blue: #1b7aad;
    --brand-blue-light: #2a8fc8;
    --accent-gold: #e9b143;
    --card-white: #ffffff;
    --ink: #1d1d1f;
  }
  html, body {
    margin: 0;
    padding: 0;
    width: 1200px;
    height: 960px;
    overflow: hidden;
    background: var(--stage);
    font-family: "Montserrat", sans-serif;
  }
  .canvas {
    position: relative;
    width: 1200px;
    height: 960px;
  }
  .card {
    position: absolute;
    width: 560px;
    height: 320px;
    border-radius: 22px;
    box-sizing: border-box;
    overflow: hidden;
  }
  /* Front */
  .card-front {
    left: 70px;
    top: 110px;
    background: var(--brand-blue);
  }
  .front-mark {
    position: absolute;
    left: 50%;
    top: 58px;
    transform: translateX(-50%);
    width: 120px;
    height: 120px;
    border-radius: 50%;
    background: var(--accent-gold);
  }
  .front-name {
    position: absolute;
    left: 0;
    right: 0;
    top: 205px;
    text-align: center;
    color: var(--card-white);
    font-weight: 800;
    font-size: 38px;
    letter-spacing: 1px;
    text-transform: uppercase;
  }
  /* Back */
  .card-back {
    left: 570px;
    top: 520px;
    background: var(--card-white);
    padding: 42px 0 0 40px;
  }
  .back-name {
    margin: 0;
    color: var(--brand-blue);
    font-weight: 800;
    font-size: 25px;
    letter-spacing: 0.5px;
    text-transform: uppercase;
  }
  .back-role,
  .back-address {
    margin: 0;
    color: var(--ink);
    font-size: 15px;
    line-height: 20px;
  }
  .back-role { margin-top: 10px; }
  .contact-list {
    list-style: none;
    margin: 18px 0 0 0;
    padding: 0;
  }
  .contact-list li {
    display: flex;
    align-items: center;
    gap: 10px;
    color: var(--ink);
    font-size: 14px;
    line-height: 22px;
  }
  .contact-icon {
    width: 13px;
    height: 13px;
    flex: none;
    fill: var(--brand-blue);
  }
  .back-mark {
    position: absolute;
    right: 40px;
    top: 60px;
    width: 180px;
    height: 180px;
    border-radius: 50%;
    background: var(--brand-blue-light);
  }
</style>
</head>
<body>
<main class="canvas">
  <section class="card card-front" aria-label="Card front">
    <div class="front-mark" aria-hidden="true"></div>
    <div class="front-name">Harborline Motors</div>
  </section>

  <section class="card card-back" aria-label="Card back">
    <h1 class="back-name">Harborline Motors</h1>
    <p class="back-role">Car Dealer Customer Service</p>
    <p class="back-address">2741 Linden Avenue<br>Shelbyville, TN 37162</p>
    <ul class="contact-list">
      <li>
        <svg class="contact-icon" viewBox="0 0 16 16" aria-hidden="true"><path d="M3.6 1.2l2.2 2.6-1.3 1.9c.9 2 2.2 3.3 4.2 4.3l1.9-1.3 2.6 2.2-1.3 2.5C6.6 13.2 2.7 9.3 1.1 2.5z"/></svg>
        (931) 555-0148
      </li>
      <li>
        <svg class="contact-icon" viewBox="0 0 16 16" aria-hidden="true"><path d="M1 5c2-2.5 12-2.5 14 0l-1 2-3-.6V5H5v1.4L2 7zM4 8h8l2 6H2z"/></svg>
        (629) 555-0173
      </li>
      <li>
        <svg class="contact-icon" viewBox="0 0 16 16" aria-hidden="true"><path d="M1 3h14v10H1zm1.5 1.2L8 8.6l5.5-4.4z"/></svg>
        harborlinemotorstn@mailbox-example.net
      </li>
      <li>
        <svg class="contact-icon" viewBox="0 0 16 16" aria-hidden="true"><circle cx="8" cy="8" r="7"/><path d="M1 8h14M8 1c3 3.5 3 10.5 0 14M8 1c-3 3.5-3 10.5 0 14" stroke="#fff" stroke-width="1" fill="none"/></svg>
        www.harborlinemotorstn.net
      </li>
    </ul>
    <div class="back-mark" aria-hidden="true"></div>
  </section>
</main>
</body>
</html>
```